Keystone Ward Security - Trade Show Booth 10x20

I need designs for an upcoming trade show booth. We want something sleek, simple that represents our brand well.

Target Market(s)

property Managers

```html
<!DOCTYPE html>
<html lang="en">
<head>
<meta charset="utf-8">
<title>Keystone Ward Security – Trade Show Backdrop</title>
<link rel="stylesheet" href="https://fonts.googleapis.com/css2?family=Exo+2:wght@600;700&family=Michroma&display=swap">
<style>
  :root {
    --ink: #2a2a2a;
    --flame: #ff3d00;
    --paper: #ffffff;
    --stage: #f1f1f1;
  }
  * { margin: 0; padding: 0; box-sizing: border-box; }
  html, body { width: 874px; height: 1200px; overflow: hidden; background: var(--stage); }
  .canvas { position: relative; width: 874px; height: 1200px; }

  .backdrop {
    position: absolute; left: 20px; top: 391px;
    width: 834px; height: 417px;
    background: var(--paper);
    box-shadow: 0 6px 22px rgba(0,0,0,.35);
    overflow: hidden;
  }

  .brand-lockup {
    position: absolute; left: 17px; top: 18px;
    display: flex; align-items: center; gap: 22px;
  }
  .brand-square { width: 64px; height: 64px; background: var(--ink); }
  .brand-name {
    font-family: "Michroma", sans-serif;
    font-size: 21px; line-height: 27px; color: var(--ink);
    text-transform: uppercase; letter-spacing: 1px;
  }

  .tagline {
    position: absolute; left: 17px; top: 127px;
    font-family: "Exo 2", sans-serif; font-weight: 600;
    font-size: 18px; color: var(--ink); letter-spacing: .3px;
  }
  .lead {
    position: absolute; left: 17px; top: 146px;
    font-family: "Exo 2", sans-serif; font-weight: 700;
    font-size: 31px; color: var(--ink);
  }
  .headline {
    position: absolute; left: 14px; top: 178px;
    font-family: "Exo 2", sans-serif; font-weight: 700;
    font-size: 70px; line-height: 58px; color: var(--flame);
    text-transform: uppercase;
  }

  .phone-band {
    position: absolute; left: 0; top: 321px; width: 100%; height: 42px;
    background: var(--flame);
  }
  .phone {
    position: absolute; left: 17px; top: 3px;
    font-family: "Michroma", sans-serif; font-size: 29px;
    color: var(--paper); letter-spacing: 1px;
  }
  .web-band {
    position: absolute; left: 0; top: 363px; width: 100%; height: 54px;
    background: var(--ink);
  }
  .web {
    position: absolute; left: 17px; top: 15px;
    font-family: "Michroma", sans-serif; font-size: 16px;
    color: var(--paper); text-transform: uppercase;
  }

  .feature-panel {
    position: absolute; left: 478px; top: 20px; width: 334px; height: 382px;
    background: var(--paper);
    display: flex; flex-direction: column; align-items: center; justify-content: center; gap: 22px;
  }
  .feature-dot { width: 46px; height: 46px; border-radius: 50%; background: var(--flame); }
  .feature-name {
    font-family: "Michroma", sans-serif; font-size: 34px; line-height: 50px;
    color: var(--ink); text-transform: uppercase; text-align: center;
  }
</style>
</head>
<body>
<main class="canvas">
  <section class="backdrop">
    <div class="brand-lockup">
      <span class="brand-square"></span>
      <p class="brand-name">Keystone Ward<br>Security</p>
    </div>

    <p class="tagline">YOUR PARTNER IN PROTECTION</p>
    <p class="lead">DELIVERING SCALABLE</p>
    <h1 class="headline">Security<br>Solutions</h1>

    <div class="phone-band"><p class="phone">801-555-0187</p></div>
    <div class="web-band"><p class="web">keystonewardsecurity.com</p></div>

    <div class="feature-panel">
      <span class="feature-dot"></span>
      <p class="feature-name">Keystone<br>Ward<br>Security</p>
    </div>
  </section>
</main>
</body>
</html>
```